Bramble Hollow Spirits Bottle Label

Bramble Hollow Spirits is a distillery and craft cocktail bar that will be located in Calgary, Alberta, Canada. Here, we create awesome hand crafted spirits like vodka, gin, rum, whiskey, brandy, liqueurs etc. We need bottle labels for 3 different initial products. The names of the products are as follows, Pepper Drift Gin (22% alc/vol), Moravel Dry Gin (40% alc/vol), and Talunet Contemporary Gin (40% alc/vol). It would be preferable to have 3 distinct labels. The alcohol by volume declaration must be on the front display of the label, without having to turn the bottle. There is a logo for Bramble Hollow Spirits I would like featured in the front around 1''x1" or 2.5cm x 2.5cm in size. Some last minute changes are being made to the logo so it is not uploaded at this moment. Abstract geometry would be a great fit for the contemporary gin and I have attached an example.Simple or complex designs both encouraged. The Pepper Drift Gin will be in the Moonea style bottle and the other two will be in Apotheker style bottles. Thank you so much to anyone interested in participating and we can't wait to hear from you. This is a great opportunity to showcase your creativity and be involved with future products!
Target Market(s)
Young professionals ages 21-30.

```html
<!DOCTYPE html>
<html lang="en">
<head>
<meta charset="utf-8">
<title>Pepper Drift Gin – Bottle Label</title>
<link rel="stylesheet" href="https://fonts.googleapis.com/css2?family=Anton&family=Federo&display=swap">
<style>
  :root {
    --canvas: #f2f2f2;
    --label-black: #050404;
    --copper: #e38a3e;
    --gold: #d89d45;
    --ember-dark: #5a1a1e;
    --ember-mid: #a2372a;
    --ember-warm: #d7692c;
    --flame-orange: #e9902c;
    --flame-yellow: #eadb3a;
  }
  * { margin: 0; padding: 0; box-sizing: border-box; }
  html, body {
    width: 1000px;
    height: 1200px;
    overflow: hidden;
    background: var(--canvas);
  }
  .label {
    position: absolute;
    left: 50px;
    top: 60px;
    width: 900px;
    height: 1080px;
    background: var(--label-black);
    font-family: "Federo", sans-serif;
    color: var(--copper);
    text-align: center;
  }
  .label-art {
    position: absolute;
    inset: 0;
    width: 900px;
    height: 1080px;
  }
  .brand-name {
    position: absolute;
    left: 0;
    right: 0;
    top: 120px;
    color: var(--gold);
    font-size: 44px;
    line-height: 1.1;
    letter-spacing: 2px;
  }
  .brand-name .brand-line { display: block; }
  .brand-name .brand-line.small {
    font-size: 30px;
    letter-spacing: 10px;
  }
  .tagline {
    position: absolute;
    left: 0; right: 0;
    top: 300px;
    font-size: 22px;
    letter-spacing: 1px;
  }
  .product-name {
    position: absolute;
    left: 0; right: 0;
    top: 348px;
    font-size: 84px;
    font-weight: 400;
    line-height: 1;
    letter-spacing: 1px;
  }
  .abv {
    position: absolute;
    left: 0; right: 0;
    top: 928px;
    font-size: 36px;
    letter-spacing: 2px;
  }
  .origin {
    position: absolute;
    left: 0; right: 0;
    top: 1008px;
    font-size: 22px;
    letter-spacing: 1px;
  }
</style>
</head>
<body>
  <main class="label">
    <svg class="label-art" viewBox="0 0 900 1080">
      <defs>
        <linearGradient id="ember-band" x1="0" y1="0" x2="0" y2="1">
          <stop offset="0" stop-color="var(--ember-mid)"/>
          <stop offset="0.5" stop-color="var(--ember-dark)"/>
          <stop offset="1" stop-color="var(--ember-mid)"/>
        </linearGradient>
        <linearGradient id="panel-fill" x1="0" y1="0" x2="1" y2="1">
          <stop offset="0" stop-color="var(--ember-mid)"/>
          <stop offset="0.5" stop-color="var(--ember-warm)"/>
          <stop offset="1" stop-color="var(--ember-dark)"/>
        </linearGradient>
        <linearGradient id="letter-fill" x1="0" y1="0" x2="1" y2="0">
          <stop offset="0" stop-color="var(--flame-orange)"/>
          <stop offset="0.55" stop-color="var(--flame-yellow)"/>
          <stop offset="1" stop-color="var(--flame-orange)"/>
        </linearGradient>
      </defs>

      <path class="side-bracket left" role="img" aria-label="Geometric pattern band, left bracket"
            fill="url(#ember-band)"
            d="M17 27 H118 V50 H80 V1030 H118 V1053 H17 Z"/>
      <path class="side-bracket right" role="img" aria-label="Geometric pattern band, right bracket"
            fill="url(#ember-band)"
            d="M883 27 H782 V50 H820 V1030 H782 V1053 H883 Z"/>

      <circle class="brand-mark" role="img" aria-label="Bramble Hollow Spirits brand mark"
              cx="450" cy="76" r="30" fill="var(--gold)"/>

      <g class="gin-panel">
        <rect role="img" aria-label="Geometric pattern panel behind product type"
              x="78" y="468" width="776" height="432" rx="22"
              fill="url(#panel-fill)" stroke="var(--label-black)" stroke-width="10"/>
        <text x="110" y="878" textLength="712" lengthAdjust="spacingAndGlyphs"
              font-family="Anton, sans-serif" font-size="420"
              fill="url(#letter-fill)" stroke="var(--label-black)" stroke-width="12"
              paint-order="stroke">GIN</text>
      </g>
    </svg>

    <div class="brand-name">
      <span class="brand-line">BRAMBLE HOLLOW</span>
      <span class="brand-line small">SPIRITS</span>
    </div>
    <p class="tagline">PREMIUM DISTILLED</p>
    <h1 class="product-name">PEPPER DRIFT</h1>
    <p class="abv">22% ALC/VOL</p>
    <p class="origin">CALGARY, ALBERTA, CANADA</p>
  </main>
</body>
</html>
```